Brisk Morsels
Business Card and Stationary Design
Brisk Morsels -
Creative Brief
Bright & Fun-filled
Gordon T Welham
Owner
41 Harlow Lane Millbrook Ridge, NJ 08637
Gord.Welham@postmailer.example
www.brisk-morsels.example
Looking for something simple, but eye-catching. Looking for a variety of different fonts/styles/backgrounds to achieve: -Seamless integration with the attached logo. -Backgrounds to enhance the "pop" of the logo. -Professional, but with a hint of fun. The Brisk Morsel will compete in the energy drink/shot industry (e.g. Tan Lynx and Nine Minute Vigor). We differentiate ourselves through superior taste and natural ingredients, creating a more satisfying experience for the energy consumer. Feel free to message me with any questions/concerns/comments.

```html
<!DOCTYPE html>
<html lang="en">
<head>
<meta charset="utf-8">
<title>Brisk Morsels – Business Card</title>
<link rel="stylesheet" href="https://fonts.googleapis.com/css2?family=Open+Sans:wght@400;600;700&display=swap">
<style>
  :root {
    --page-bg: #ece9e4;
    --card-bg: #ffffff;
    --brand-brown: #5a3620;
    --brand-orange: #e8892b;
    --text-dark: #3a2a20;
    --text-muted: #6b5d52;
  }
  * { box-sizing: border-box; margin: 0; padding: 0; }
  html, body { width: 1200px; height: 818px; overflow: hidden; }
  body {
    background: var(--page-bg);
    font-family: "Open Sans", Arial, sans-serif;
    position: relative;
  }
  .card {
    position: absolute;
    width: 520px;
    height: 300px;
    background: var(--card-bg);
    border-radius: 16px;
    box-shadow: 0 6px 18px rgba(0,0,0,0.12);
  }
  .card--front { left: 50px; top: 259px; }
  .card--back  { left: 630px; top: 259px; }

  .brand {
    position: absolute;
    display: flex;
    align-items: center;
    gap: 10px;
    color: var(--brand-brown);
    font-weight: 700;
    white-space: nowrap;
  }
  .brand__dot {
    border-radius: 50%;
    background: var(--brand-orange);
    flex: none;
  }
  .card--front .brand { right: 30px; top: 62px; font-size: 30px; }
  .card--front .brand__dot { width: 26px; height: 26px; }
  .card--back .brand { left: 50%; top: 50%; transform: translate(-50%, -50%); font-size: 44px; }
  .card--back .brand__dot { width: 36px; height: 36px; }

  .contact {
    position: absolute;
    left: 30px;
    top: 150px;
    color: var(--text-dark);
    font-size: 11px;
    line-height: 1.45;
  }
  .contact__name { font-size: 17px; font-weight: 700; color: var(--text-dark); }
  .contact__name .first { color: var(--brand-orange); }
  .contact__role { color: var(--text-muted); margin-bottom: 12px; }
  .contact__address { margin-bottom: 10px; }
  .contact__label { color: var(--brand-orange); }
  .contact__sep { color: var(--text-muted); margin: 0 6px; }
  .contact__web { color: var(--brand-orange); margin-top: 4px; }
</style>
</head>
<body>
  <section class="card card--front" aria-label="Business card front">
    <div class="brand"><span class="brand__dot"></span>Brisk Morsels</div>
    <div class="contact">
      <p class="contact__name"><span class="first">Gordon</span> T Welham</p>
      <p class="contact__role">Owner</p>
      <p class="contact__address">41 Harlow Lane<br>Millbrook Ridge, NJ 08637</p>
      <p class="contact__lines"><span class="contact__label">Cell:</span> (555) 014-2290<span class="contact__sep">|</span><span class="contact__label">Email:</span> Gord.Welham@postmailer.example</p>
      <p class="contact__web">www.brisk-morsels.example</p>
    </div>
  </section>

  <section class="card card--back" aria-label="Business card back">
    <div class="brand"><span class="brand__dot"></span>Brisk Morsels</div>
  </section>
</body>
</html>
```